Venture Capital firm needs modern business cards

We are a Venture Capital firm within financial services/Asset management. The industry generally has basic business cards with black, blue and maybe green/yellow design elements.
Our firm has a four-colour swoosh logo. We are based in London and want to stand out, just a little bit!, from the crowd. Our company is called MOBRA Holdings and the 'C' stands for collaboration thus using pixelfair is a natural portal for our business card design competition. Our logo came via pixelfair too!
We use 'Venture Partner in Asset Management' as our tagline and this is Trademark registered. We operate in a conservative industry and we should not overstep our mark. The logo is colorful as it is and therefore the rest of the design should not be too fanciful.
The objective is twofold: make our logo element stick and memorable with our audience, whilst representing a conservative yet young image.
Updates
The Business Card obviously needs a field for Name, Surname, Job Title, Adress fields: Street, City, Postcode, Country, telefone and cell number, website address, etc.
We have uploaded the ai file. We trust that these are OK. If not, please advise.
Reason: We have have been busy with a client engagement. We will set the project as Guaranteed in return for the troubles we cause. Apologies for the confusion.
Thank you all for these great and creative design suggestions. The team is very happy with a number of your ideas! We will be in touch tomorrow to give individual feedback before the project closes on Friday. We look forward to working with some of you to narrow down your creations. Thank you, MOBRA Holdings team.
All,
Target Market(s)
Financial Services Professionals, Investors, Media, 35-70 years, mainly male, well educated
Industry/Entity Type
Conservative
Requirements
Must have
- We must make use of our logo and potential tagline 'Venture Partner in Asset Management' as we are establishing a new Brand and new company in the market.
We can use 'MOBRA', 'MOBRA Holdings', and 'MOBRA Holdings'+tagline 'Venture Partner in Asset Management' or simply the four-colour swoosh plus the name of the company as part of the text. (see files)
All design elements are available in black or grey-scale if required. (grey scale swoosh attached).
Due to regulation we must have the following wording on the card in small print 'MOBRA Holdings is an Appointed Representative of Warbeck Ledger Advisory Limited, which is authorised by the Monetary Standards Bureau'.
Nice to have
- We would consider designs that make use of different printing techniques such embossing/debossing, UV spot etc.
We attach our colour palette in the files section for your reference.
Should not have
- The font we use for our company name is 'EXO' so do not use a font style that clashes with the corporate fonts, please.
Do not use other design elements than the ones we provide in the file library as part of this project.

```html
<!DOCTYPE html>
<html lang="en">
<head>
<meta charset="utf-8">
<title>MOBRA Holdings – Business Card</title>
<link href="https://fonts.googleapis.com/css2?family=Arimo:wght@400;700&family=Roboto+Condensed:wght@700&display=swap" rel="stylesheet">
<style>
  :root {
    --backdrop: #e9e9ea;
    --card: #fbfbfa;
    --brand-green: #8cc63f;
    --ink-grey: #5f6062;
    --soft-grey: #8a8b8d;
    --icon-grey: #9a9b9d;
    --logo-grey: #6d6e71;
  }
  * { box-sizing: border-box; margin: 0; padding: 0; }
  html, body {
    width: 1200px; height: 800px; overflow: hidden;
    background: var(--backdrop);
    font-family: "Arimo", Arial, sans-serif;
  }
  .canvas {
    width: 1200px; height: 800px;
    display: flex; align-items: center; justify-content: center; gap: 40px;
  }
  .card {
    width: 540px; height: 320px;
    background: var(--card);
    box-shadow: 0 2px 10px rgba(0,0,0,.12);
    position: relative;
  }
  /* back side */
  .card--back { display: flex; align-items: center; justify-content: center; }
  .back-mark { display: flex; align-items: center; gap: 14px; }
  .back-mark__dot { width: 34px; height: 34px; border-radius: 50%; background: var(--brand-green); }
  .back-mark__name { font-size: 56px; font-weight: 700; color: var(--logo-grey); letter-spacing: 1px; }
  /* front side */
  .card--front {
    display: flex; flex-direction: column; align-items: center;
    padding-top: 18px; text-align: center; color: var(--ink-grey);
  }
  .brand { display: flex; align-items: center; gap: 8px; }
  .brand__dot { width: 16px; height: 16px; border-radius: 50%; background: var(--brand-green); }
  .brand__text { display: flex; flex-direction: column; align-items: flex-end; }
  .brand__name { font-size: 28px; font-weight: 700; color: var(--logo-grey); letter-spacing: .5px; line-height: 1; }
  .brand__sub { font-size: 8px; color: var(--soft-grey); letter-spacing: 2.5px; line-height: 1; margin-top: 2px; }
  .tagline { font-size: 8.5px; color: var(--soft-grey); letter-spacing: .4px; line-height: 1; margin-top: 5px; }
  .person__name {
    font-family: "Roboto Condensed", "Arial Narrow", sans-serif;
    font-size: 23px; color: var(--brand-green); line-height: 1; margin-top: 7px;
  }
  .person__role { font-size: 13px; color: var(--soft-grey); margin-top: 2px; line-height: 1.1; }
  .contact { margin-top: 8px; display: flex; flex-direction: column; align-items: center; gap: 5px; }
  .contact__item { display: flex; flex-direction: column; align-items: center; gap: 3px; font-size: 12px; line-height: 1.1; }
  .contact__label { color: var(--soft-grey); }
  .contact__sep { margin: 0 6px; color: var(--icon-grey); }
  .contact__icon { width: 14px; height: 14px; fill: none; stroke: var(--icon-grey); stroke-width: 1.4; }
  .contact__icon--filled { fill: var(--icon-grey); stroke: none; }
  .contact__address { font-style: normal; }
  .legal {
    position: absolute; left: 0; right: 0; bottom: 7px;
    font-size: 6.4px; color: var(--soft-grey); text-align: center;
  }
</style>
</head>
<body>
<main class="canvas">
  <section class="card card--back" aria-label="Card back">
    <div class="back-mark">
      <span class="back-mark__dot"></span>
      <span class="back-mark__name">MOBRA</span>
    </div>
  </section>

  <section class="card card--front" aria-label="Card front">
    <div class="brand">
      <span class="brand__dot"></span>
      <div class="brand__text">
        <span class="brand__name">MOBRA</span>
        <span class="brand__sub">HOLDINGS</span>
      </div>
    </div>
    <p class="tagline">Venture Partner in Asset Management™</p>
    <h1 class="person__name">DANIEL ASHCOMBE</h1>
    <p class="person__role">Graphic designer</p>

    <div class="contact">
      <div class="contact__item">
        <svg class="contact__icon" viewBox="0 0 14 14" aria-hidden="true"><rect x="3.5" y="1" width="7" height="12" rx="1"/><line x1="6" y1="11" x2="8" y2="11"/></svg>
        <span><span class="contact__label">T</span> +44 20 7946 0321<span class="contact__sep">|</span><span class="contact__label">M</span> +44 7700 900 418</span>
      </div>
      <div class="contact__item">
        <svg class="contact__icon" viewBox="0 0 14 14" aria-hidden="true"><rect x="1" y="3" width="12" height="8"/><polyline points="1,3 7,8 13,3"/></svg>
        <span>http://www.mobra.net</span>
      </div>
      <div class="contact__item">
        <svg class="contact__icon contact__icon--filled" viewBox="0 0 14 14" aria-hidden="true"><path d="M7 1a4 4 0 0 0-4 4c0 3 4 8 4 8s4-5 4-8a4 4 0 0 0-4-4zm0 5.5A1.5 1.5 0 1 1 7 3.5a1.5 1.5 0 0 1 0 3z"/></svg>
        <address class="contact__address">48 Halden Row<br>Elmridge Park<br>London city<br>EC2V 7HQ<br>United Kingdom</address>
      </div>
    </div>

    <p class="legal">MOBRA Holdings is an Appointed Representative of Warbeck Ledger Advisory Limited, which is authorised by the Monetary Standards Bureau</p>
  </section>
</main>
</body>
</html>
```